Brightwell Rx Pass reinvent our website.

Our Website is outdated and needs an overhaul, in every aspect. We assist individuals that have little or no prescription coverage and allow them to receive a discount ranging from 33% up to 78% for free. In the beginning we utilized pharmacies to spread the word, but times have a changed. We are looking for a modern and clean site. We are open to anything, image, logo etc.

Target Market(s)

Anyone regardless of residency, age or income. This program is designed to assist those that have NO prescription coverage or for those whose particular prescription may not be covered by insurance.

Industry/Entity Type

Pharmaceutical

Coding

Coded - Design and coding required

Number of Pages Required

4 page

Requirements
Must have
• -The two MUST haves are the pharmacy locators & drug pricing. If you can combine the 2, even better.
• -a ongoing counter/tally on the 1stpage reflecting the amount of money we are saving customers. http://plumtreemarket.example/item/animated-counters-v-20-edge-animate-collection/full_screen_preview/52970314
• -on a smart phone the ability to view the information that is needed to get the actual discount for the medication.
Nice to have
• animated tutorial showing how to use the card
• health blog

```html
<!DOCTYPE html>
<html lang="en">
<head>
<meta charset="utf-8">
<title>Brightwell Rx Pass</title>
<link rel="stylesheet" href="https://fonts.googleapis.com/css2?family=Open+Sans:ital,wght@0,400;0,600;0,700;1,400&family=Arimo:ital,wght@0,400;0,700;1,400&display=swap">
<style>
:root{
  --blue:#1d5ea8;
  --blue-dark:#164c8c;
  --blue-band:#2a6db5;
  --red:#e8262b;
  --text:#3a3a3a;
  --muted:#666;
  --light:#f2f2f2;
  --line:#dcdcdc;
  --white:#fff;
}
*{box-sizing:border-box;margin:0;padding:0}
html,body{width:1200px;height:2550px;overflow:hidden}
body{font-family:"Arimo",Arial,sans-serif;color:var(--text);background:var(--white);position:relative}

/* header */
.site-header{position:absolute;left:0;top:0;width:1200px;height:116px;background:var(--white)}
.brand{position:absolute;left:102px;top:36px;display:flex;align-items:center;gap:12px}
.brand-dot{width:34px;height:34px;border-radius:50%;background:var(--blue)}
.brand-name{font-family:"Open Sans",sans-serif;font-weight:700;font-size:30px;color:var(--blue);letter-spacing:-.3px}
.contact{position:absolute;display:flex;align-items:center;gap:14px;font-size:12px;color:#333}
.contact.address{left:524px;top:38px;font-weight:700;line-height:20px;letter-spacing:.3px}
.contact.phone{left:838px;top:34px}
.phone-label{font-size:12px;color:#555;letter-spacing:.4px}
.phone-number{font-size:17px;font-weight:700;color:#333;margin-top:4px;letter-spacing:.4px}
.header-divider{position:absolute;left:806px;top:10px;width:1px;height:92px;background:var(--line)}

/* nav */
.main-nav{position:absolute;left:0;top:116px;width:1200px;height:51px;background:var(--blue)}
.main-nav ul{list-style:none;display:flex;position:absolute;left:130px;top:0;height:51px;align-items:center}
.main-nav li{font-size:12px;color:var(--white);font-family:"Open Sans",sans-serif;letter-spacing:.3px;margin-right:46px;white-space:nowrap}
.search{position:absolute;left:866px;top:122px;width:181px;height:38px;background:var(--white);border-radius:3px;font-size:12px;color:#999;padding:12px 14px}
.search svg{position:absolute;right:10px;top:10px}

/* hero */
.hero{position:absolute;left:0;top:167px;width:1200px;height:489px;background:linear-gradient(110deg,#c8d6e2 0%,#e2e9ef 35%,#b7c9d6 60%,#d8e2ea 100%)}
.hero-panel{position:absolute;left:102px;top:84px;width:530px;height:258px;background:rgba(255,255,255,.85);border-left:5px solid var(--blue);padding:18px 16px}
.hero-title{font-family:"Open Sans",sans-serif;font-weight:700;font-size:22px;color:var(--red);letter-spacing:.3px;white-space:nowrap}
.hero-copy{font-size:14px;line-height:24px;color:#333;margin-top:8px;white-space:nowrap}
.hero-copy b{color:var(--red)}
.pill{display:inline-flex;height:38px;border-radius:19px;overflow:hidden;font-family:"Open Sans",sans-serif;font-weight:700;font-size:14px}
.pill .a{background:var(--blue);color:var(--white);padding:0 12px 0 16px;display:flex;align-items:center;border-radius:19px 0 0 19px}
.pill .b{color:var(--red);border:1.5px solid var(--red);border-left:none;padding:0 18px 0 10px;display:flex;align-items:center;border-radius:0 19px 19px 0;background:var(--white)}
.hero-panel .pill{margin-top:14px;height:36px}

/* price + pharmacy lookup */
.lookup{position:absolute;left:102px;top:372px;width:996px;height:70px;background:rgba(255,255,255,.92);border-left:5px solid var(--red);display:flex;align-items:center;gap:14px;padding:0 16px}
.lookup-label{font-family:"Open Sans",sans-serif;font-weight:700;font-size:14px;color:var(--blue);white-space:nowrap;line-height:18px}
.lookup-field{height:40px;border:1px solid #cfcfcf;background:var(--white);font-size:13px;color:#999;display:flex;align-items:center;padding:0 12px;white-space:nowrap}
.lookup-field.drug{width:300px}
.lookup-field.zip{width:170px}
.lookup-btn{height:40px;background:var(--red);color:var(--white);font-family:"Open Sans",sans-serif;font-weight:700;font-size:13px;display:flex;align-items:center;gap:8px;padding:0 16px;white-space:nowrap}

/* mission */
.mission{position:absolute;left:0;top:656px;width:1200px;height:319px;text-align:center}
.mission .pill{position:absolute;left:502px;top:30px;height:48px;font-size:17px;border-radius:24px}
.mission .pill .a{padding:0 20px 0 26px;border-radius:24px 0 0 24px}
.mission .pill .b{padding:0 10px 0 8px;border-radius:0 24px 24px 0}
.mission-text{position:absolute;left:140px;top:94px;width:920px;font-size:13px;line-height:22px;color:#444}
.mission-text p+p{margin-top:12px}
.savings{position:absolute;left:0;top:194px;width:1200px;display:flex;justify-content:center;align-items:center;gap:14px}
.savings-label{font-family:"Open Sans",sans-serif;font-weight:700;font-size:14px;color:var(--blue);letter-spacing:.3px}
.savings-digits{display:flex;gap:4px;font-family:"Open Sans",sans-serif;font-weight:700;font-size:20px;color:var(--white)}
.savings-digits span{background:var(--blue);width:26px;height:36px;display:flex;align-items:center;justify-content:center;border-radius:3px}
.savings-digits span.sep{background:none;color:var(--blue);width:8px}
.btn-red{display:inline-flex;align-items:center;gap:8px;background:var(--red);color:var(--white);font-family:"Open Sans",sans-serif;font-weight:700;font-size:13px;padding:0 14px;height:36px}
.mission .btn-red{position:absolute;left:544px;top:256px}

/* video */
.how-to{position:absolute;left:0;top:975px;width:1200px;height:558px;background:linear-gradient(180deg,#2c2f38 0%,#1b1d24 55%,#3a3025 100%)}
.section-title{font-family:"Open Sans",sans-serif;font-weight:700;font-size:19px;text-align:center;letter-spacing:.3px}
.how-to .section-title{position:absolute;left:0;top:24px;width:1200px;color:var(--white)}
.how-to-copy{position:absolute;left:200px;top:68px;width:800px;text-align:center;font-style:italic;font-size:13px;line-height:23px;color:#e6e6e6}
.video{position:absolute;left:185px;top:135px;width:832px;height:362px;background:linear-gradient(120deg,#5d6a6b 0%,#b9bcb4 45%,#d9d2c8 70%,#8e9aa2 100%)}
.play{position:absolute;left:372px;top:135px}

/* prices */
.prices{position:absolute;left:0;top:1533px;width:1200px;height:380px;background:var(--blue-band)}
.prices .section-title{position:absolute;left:0;top:38px;width:1200px;color:var(--white);font-size:20px}
.price-card{position:absolute;top:102px;width:177px;height:227px;background:var(--white);text-align:center}
.price-card .top{height:98px;background:var(--light);padding-top:18px;font-size:17px;color:#444}
.price-card .hex{position:absolute;left:48px;top:50px}
.price-card .amount{position:absolute;left:0;top:85px;width:177px;font-size:20px;color:var(--red)}
.price-card .rule{position:absolute;left:16px;top:155px;width:145px;height:1px;background:var(--line)}
.price-card .qty{position:absolute;left:0;top:170px;width:177px;font-size:16px;color:#666}

/* blog */
.blog{position:absolute;left:0;top:1913px;width:1200px;height:561px}
.blog .section-title{position:absolute;left:0;top:44px;width:1200px;color:var(--blue);font-size:19px}
.blog-sub{position:absolute;left:0;top:82px;width:1200px;text-align:center;font-style:italic;font-size:13px;color:#444}
.post{position:absolute;top:141px;width:294px;height:301px;background:var(--light)}
.post-image{height:170px}
.post h3{font-size:15px;font-weight:700;color:#222;padding:14px 6px 0 6px}
.post p{font-size:13px;line-height:21px;color:#555;padding:6px 6px 0 6px}
.post-meta{position:absolute;left:6px;right:6px;bottom:0;height:42px;border-top:1.5px dotted #bbb;display:flex;align-items:center;font-size:13px;color:var(--red)}
.post-meta .date{margin-left:4px;flex:1}
.post-meta span{display:inline-flex;align-items:center;gap:5px}
.post-meta .comments{margin-left:16px;margin-right:4px}
.blog .btn-red{position:absolute;left:527px;top:479px;height:37px}

/* footer */
.site-footer{position:absolute;left:0;top:2474px;width:1200px;height:76px;background:var(--blue)}
.copyright{position:absolute;left:100px;top:30px;font-size:13px;color:var(--white)}
.social{position:absolute;left:968px;top:20px;display:flex;gap:12px}
.social span{width:36px;height:36px;border-radius:50%;border:2px solid var(--white);display:block}
</style>
</head>
<body>

<header class="site-header">
  <div class="brand"><span class="brand-dot"></span><span class="brand-name">Brightwell Rx Pass</span></div>
  <div class="contact address">
    <svg width="24" height="32" viewBox="0 0 24 32"><path d="M12 1C6 1 2 5.5 2 11c0 7.5 10 19 10 19s10-11.5 10-19C22 5.5 18 1 12 1z" fill="none" stroke="#e8262b" stroke-width="2.5"/><circle cx="12" cy="11" r="4" fill="#e8262b"/></svg>
    <div>2710 LARKSPUR AVENUE #210<br>EASTBRIDGE OR97418</div>
  </div>
  <div class="header-divider"></div>
  <div class="contact phone">
    <svg width="36" height="34" viewBox="0 0 36 34"><rect x="3" y="2" width="17" height="30" rx="3" fill="none" stroke="#e8262b" stroke-width="2.5"/><circle cx="11.5" cy="27" r="1.6" fill="#e8262b"/><path d="M25 11q3 6 0 12M29 8q5 9 0 18" fill="none" stroke="#e8262b" stroke-width="2.2" stroke-linecap="round"/></svg>
    <div><div class="phone-label">CALL FOR A FREE CONSULTATION</div><div class="phone-number">541-308-2274</div></div>
  </div>
</header>

<nav class="main-nav">
  <ul><li>HOME</li><li>ABOUT US</li><li>DRUG PRICING</li><li>PHARMACY LOCATOR</li><li>GALLERY</li><li>CONTACTS</li></ul>
</nav>
<div class="search">Search..
  <svg width="20" height="20" viewBox="0 0 20 20"><circle cx="8" cy="8" r="6" fill="none" stroke="#666" stroke-width="2.2"/><path d="M12.5 12.5l6 6" stroke="#666" stroke-width="2.6" stroke-linecap="round"/></svg>
</div>

<section class="hero" role="img" aria-label="Photo of hands holding out blister packs of colourful prescription tablets">
  <div class="hero-panel">
    <h1 class="hero-title">FREE PRESCRIPTION ASSISTANCE PROGRAM</h1>
    <div class="hero-copy">
      Completely Free prescription Assistance Program Lowest Price logic to<br>
      guarantee that you get the best deal on your prescriptions<br>
      Instant Printable membership card ready to use<br>
      Saving of up to <b>78%</b> at more than <b>60,000</b> national and regional pharmacies<br>
      This card is pre-activate and can be used immediately.
    </div>
    <div class="pill"><span class="a">GET FREE</span><span class="b">CARD</span></div>
  </div>
  <form class="lookup">
    <div class="lookup-label">DRUG PRICING &amp;<br>PHARMACY LOCATOR</div>
    <div class="lookup-field drug">Enter drug name</div>
    <div class="lookup-field zip">ZIP code</div>
    <div class="lookup-btn">FIND PRICES NEAR ME <svg width="7" height="10" viewBox="0 0 7 10"><path d="M0 0l7 5-7 5z" fill="#fff"/></svg></div>
  </form>
</section>

<section class="mission">
  <div class="pill"><span class="a">OUR</span><span class="b">MISSION</span></div>
  <div class="mission-text">
    <p>Lorem ipsum dolor sit amet, consectetur adipiscing elit, sed do eiusmod tempor incididunt ut labore et dolore magna aliqua. Ut enim ad minim velit esse cillum dolore eu fugiat nulla pariatur. Excepteur sint occaecat cupidatat non proident,</p>
    <p>sunt in culpa qui officia deserunt mollit anim id est laborum Sed ut perspiciatis unde omnis iste natus error sit voluptatem doloremque.</p>
  </div>
  <div class="savings">
    <span class="savings-label">SAVED FOR OUR MEMBERS SO FAR</span>
    <div class="savings-digits"><span class="sep">$</span><span>1</span><span>2</span><span class="sep">,</span><span>4</span><span>8</span><span>6</span><span class="sep">,</span><span>9</span><span>0</span><span>5</span></div>
  </div>
  <a class="btn-red">READ MORE <svg width="7" height="10" viewBox="0 0 7 10"><path d="M0 0l7 5-7 5z" fill="#fff"/></svg></a>
</section>

<section class="how-to">
  <h2 class="section-title">HOW TO USE THE CARD</h2>
  <p class="how-to-copy">Lorem ipsum dolor sit amet, consectetur adipiscing elit, sed do eiusmod tempor incididunt ut labore et dolore magna aliqua. Ut enim ad minim velit esse cillum dolore eu fugiat nulla pariatur.</p>
  <div class="video" role="img" aria-label="Video still of a hand holding up a blank discount card in a pharmacy">
    <svg class="play" width="88" height="88" viewBox="0 0 88 88"><circle cx="44" cy="44" r="44" fill="#e8262b"/><path d="M34 26l30 18-30 18z" fill="#fff"/></svg>
  </div>
</section>

<section class="prices">
  <h2 class="section-title">PRICES</h2>
  <div class="price-card" style="left:100px"><div class="top">2Weeks Supply</div><svg class="hex" width="81" height="90" viewBox="0 0 81 90"><path d="M40.5 2L79 24v42L40.5 88 2 66V24z" fill="#fff" stroke="#e4e4e4" stroke-width="2"/></svg><div class="amount">$40</div><div class="rule"></div><div class="qty">20 Tablets</div></div>
  <div class="price-card" style="left:306px"><div class="top">4Weeks Supply</div><svg class="hex" width="81" height="90" viewBox="0 0 81 90"><path d="M40.5 2L79 24v42L40.5 88 2 66V24z" fill="#fff" stroke="#e4e4e4" stroke-width="2"/></svg><div class="amount">$80</div><div class="rule"></div><div class="qty">40 Tablets</div></div>
  <div class="price-card" style="left:512px"><div class="top">6Weeks Supply</div><svg class="hex" width="81" height="90" viewBox="0 0 81 90"><path d="M40.5 2L79 24v42L40.5 88 2 66V24z" fill="#fff" stroke="#e4e4e4" stroke-width="2"/></svg><div class="amount">$100</div><div class="rule"></div><div class="qty">60 Tablets</div></div>
  <div class="price-card" style="left:718px"><div class="top">8Weeks Supply</div><svg class="hex" width="81" height="90" viewBox="0 0 81 90"><path d="M40.5 2L79 24v42L40.5 88 2 66V24z" fill="#fff" stroke="#e4e4e4" stroke-width="2"/></svg><div class="amount">$120</div><div class="rule"></div><div class="qty">80 Tablets</div></div>
  <div class="price-card" style="left:923px"><div class="top">10Weeks Supply</div><svg class="hex" width="81" height="90" viewBox="0 0 81 90"><path d="M40.5 2L79 24v42L40.5 88 2 66V24z" fill="#fff" stroke="#e4e4e4" stroke-width="2"/></svg><div class="amount">$140</div><div class="rule"></div><div class="qty">100 Tablets</div></div>
</section>

<section class="blog">
  <h2 class="section-title">HEALTH BLOG</h2>
  <p class="blog-sub">Read our regular blog post for helpful thought and inspirations.</p>

  <article class="post" style="left:102px">
    <div class="post-image" role="img" aria-label="Photo of medical staff in a bright clinic" style="background:linear-gradient(120deg,#e9eef2,#c9d9e3 60%,#dfe8ee)"></div>
    <h3>Blog Name 1</h3>
    <p>sed do eiusmod tempor incididunt ut labore et dolore magna aliqua.</p>
    <div class="post-meta"><span class="date">09,11,2016</span>
      <span><svg width="12" height="13" viewBox="0 0 12 13"><circle cx="6" cy="3.5" r="3" fill="#555"/><path d="M0 13c0-4 2.5-6 6-6s6 2 6 6z" fill="#555"/></svg>admin</span>
      <span class="comments"><svg width="14" height="12" viewBox="0 0 14 12"><path d="M7 1C3.5 1 1 3 1 5.3c0 1.3.8 2.5 2 3.2L2.5 11l3-1.7c.5.1 1 .1 1.5.1 3.5 0 6-2 6-4.1S10.5 1 7 1z" fill="none" stroke="#555" stroke-width="1.5"/></svg>0</span></div>
  </article>

  <article class="post" style="left:452px">
    <div class="post-image" role="img" aria-label="Photo of green and red capsules on a white surface" style="background:linear-gradient(150deg,#f4f4f0,#c9cf9a 50%,#e6e6e0)"></div>
    <h3>Blog Name 2</h3>
    <p>sed do eiusmod tempor incididunt ut labore et dolore magna aliqua.</p>
    <div class="post-meta"><span class="date">09,11,2016</span>
      <span><svg width="12" height="13" viewBox="0 0 12 13"><circle cx="6" cy="3.5" r="3" fill="#555"/><path d="M0 13c0-4 2.5-6 6-6s6 2 6 6z" fill="#555"/></svg>admin</span>
      <span class="comments"><svg width="14" height="12" viewBox="0 0 14 12"><path d="M7 1C3.5 1 1 3 1 5.3c0 1.3.8 2.5 2 3.2L2.5 11l3-1.7c.5.1 1 .1 1.5.1 3.5 0 6-2 6-4.1S10.5 1 7 1z" fill="none" stroke="#555" stroke-width="1.5"/></svg>0</span></div>
  </article>

  <article class="post" style="left:802px">
    <div class="post-image" role="img" aria-label="Photo of white pills and an orange bottle on a heart-rate chart" style="background:linear-gradient(120deg,#f7f1ef,#ecdcd8 55%,#f3c8a0)"></div>
    <h3>Blog Name 3</h3>
    <p>sed do eiusmod tempor incididunt ut labore et dolore magna aliqua.</p>
    <div class="post-meta"><span class="date">09,11,2016</span>
      <span><svg width="12" height="13" viewBox="0 0 12 13"><circle cx="6" cy="3.5" r="3" fill="#555"/><path d="M0 13c0-4 2.5-6 6-6s6 2 6 6z" fill="#555"/></svg>admin</span>
      <span class="comments"><svg width="14" height="12" viewBox="0 0 14 12"><path d="M7 1C3.5 1 1 3 1 5.3c0 1.3.8 2.5 2 3.2L2.5 11l3-1.7c.5.1 1 .1 1.5.1 3.5 0 6-2 6-4.1S10.5 1 7 1z" fill="none" stroke="#555" stroke-width="1.5"/></svg>0</span></div>
  </article>

  <a class="btn-red">VIEW MORE POST <svg width="7" height="10" viewBox="0 0 7 10"><path d="M0 0l7 5-7 5z" fill="#fff"/></svg></a>
</section>

<footer class="site-footer">
  <p class="copyright">Copyright © 2013.All right reserved</p>
  <div class="social" aria-label="Social links"><span></span><span></span><span></span></div>
</footer>

</body>
</html>
```